Gift Box (layout attached) Packaging Design for sweet shop!

We are a Brazilian company interested in making the best Brigadeiros (Brazilian traditional sweet) in the country and also helping this little pieces of heaven become world famous one day! LOL.... Please help us with our official packaging so that we can transform this sweets into heart warming and eye catching GIFTS, instead of just a normal package of confectionery... ALL INFO on the PPT Attached! Pls refer to the box shape on the layout attached and create your design on it!! Tks!!!
Updates

Dear designers!

I have uploaded three pics of the gift boxes i like the most from my references to make it easier for you to spot them!

I really like the "clean style" of the dotted one from hop tart (not the one with smiling faces, the other one), the creative patterns of the butterfly boxes and the colour pallette of my currently used packages.

If you have any questions pls lemme know!!

Tks for participating!!!! Looking fwd to all your designs! And pls remember to use the logo and the box shape provided!

Target Market(s)

People interested im giving gourmet and elegant gifts, people who would like to pamper themselves with some sweets, people looking to feel good about the product they just bought.. the package should look just like a gift itself, kinda similar to how people view cupcake packagings in other countries.

Industry/Entity Type

It Company

Requirements
Must have
• please create your design on the box layout attached!
Logo in a visible place
The following allergy warning text (may be small font) : “Produto para consumo imediato. Pode conter glúten, lactose, castanhas e similares.”
Contact details:
Av. Santa Luzia, 2187
Vila Corvo – São Paulo
Tel: (11) 3721-6093
oi@casadotrufinho.com.br
www.casadotrufinho.com.br
Facebook.com/casadotrufinhoquitutesfinos
Nice to have
• be suitable for men an women (despite the fact that the shop is really feminine, the packaging may contain other colours rather than just pink and lilac... like green, blue, gray... but it has to be vintage looking and in harmony with the shop look and feel (pics on the ppt attached)
Should not have
• characters (not even retro ones)

```html
<!DOCTYPE html>
<html lang="pt-BR">
<head>
<meta charset="utf-8">
<title>Casa do Trufinho – Gift Box Dieline</title>
<link rel="stylesheet" href="https://fonts.googleapis.com/css2?family=Chango&family=Cormorant+Garamond:ital,wght@1,500;1,600&display=swap">
<style>
  :root {
    --wine: #6b1038;
    --wine-deep: #3a0a22;
    --blush: #fba9d6;
    --blush-light: #ffd3ec;
    --band-pink: #f58ccb;
    --white: #ffffff;
    --tab-line: #9a9a9a;
  }
  html, body {
    margin: 0;
    padding: 0;
    overflow: hidden;
    background: var(--white);
  }
  .dieline {
    position: relative;
    width: 1200px;
    height: 569px;
    background: var(--white);
    overflow: hidden;
  }
  .dieline-shapes {
    position: absolute;
    inset: 0;
  }
  .brand-mark {
    position: absolute;
    top: 300px;
    width: 334px;
    display: flex;
    align-items: center;
    justify-content: center;
    gap: 8px;
    font-family: "Chango", "Arial Black", sans-serif;
    font-size: 25px;
    color: var(--wine);
    white-space: nowrap;
  }
  .brand-mark::before {
    content: "";
    width: 14px;
    height: 14px;
    border-radius: 50%;
    background: var(--wine);
  }
  .brand-mark.front-a { left: 46px; }
  .brand-mark.front-b { left: 605px; }
  .side-story {
    position: absolute;
    left: 390px;
    top: 284px;
    width: 205px;
    text-align: center;
    font-family: "Cormorant Garamond", Georgia, serif;
    font-style: italic;
    color: var(--blush);
  }
  .side-story h2 {
    margin: 0 0 3px;
    font-size: 12.5px;
    font-weight: 600;
    letter-spacing: 0.3px;
  }
  .side-story p {
    margin: 0;
    font-size: 6.6px;
    line-height: 9.6px;
    font-weight: 500;
  }
</style>
</head>
<body>
<main class="dieline">
  <svg class="dieline-shapes" width="1200" height="569" viewBox="0 0 1200 569" xmlns="http://www.w3.org/2000/svg">
    <defs>
      <linearGradient id="band-stripes" x1="0" y1="0" x2="0" y2="1">
        <stop offset="0" stop-color="#f9a3d6"/>
        <stop offset="0.5" stop-color="#ffd0ea"/>
        <stop offset="1" stop-color="var(--band-pink)"/>
      </linearGradient>
      <linearGradient id="band-shadow" x1="0" y1="0" x2="0" y2="1">
        <stop offset="0" stop-color="#5a1232"/>
        <stop offset="1" stop-color="var(--wine-deep)"/>
      </linearGradient>
      <radialGradient id="dots-soft" cx="0.5" cy="0.5" r="0.5">
        <stop offset="0" stop-color="#f4b6da" stop-opacity="0.75"/>
        <stop offset="1" stop-color="#f4b6da" stop-opacity="0"/>
      </radialGradient>
      <radialGradient id="dots-soft-light" cx="0.5" cy="0.5" r="0.5">
        <stop offset="0" stop-color="#ffffff" stop-opacity="0.6"/>
        <stop offset="1" stop-color="#ffffff" stop-opacity="0"/>
      </radialGradient>
      <radialGradient id="logo-glow" cx="0.5" cy="0.5" r="0.5">
        <stop offset="0" stop-color="#ffffff" stop-opacity="0.9"/>
        <stop offset="1" stop-color="#ffffff" stop-opacity="0"/>
      </radialGradient>

      <g id="front-panel">
        <path class="front-body" fill="var(--wine)" fill-rule="evenodd"
          d="M82 28 L345 28 Q360 28 362 40 Q378 38 378 58 Q374 70 366 76
             Q372 150 380 262 L380 390 Q366 400 366 420 Q370 438 380 440 L380 548
             L64 548 Q54 548 54 538 L56 450 Q68 440 66 420 Q62 398 46 392
             L46 262 Q52 150 62 76 Q56 70 54 58 Q54 40 68 38 Q70 28 82 28 Z
             M130 74 L300 74 Q310 74 310 84 L310 118 Q310 126 300 126 L130 126 Q120 126 120 118 L120 84 Q120 74 130 74 Z"/>
        <g role="img" aria-label="Scattered pink and white dot pattern">
          <ellipse cx="300" cy="200" rx="95" ry="80" fill="url(#dots-soft)"/>
          <ellipse cx="150" cy="170" rx="80" ry="50" fill="url(#dots-soft)" opacity="0.6"/>
        </g>
        <rect x="46" y="262" width="334" height="123" fill="url(#band-stripes)"/>
        <ellipse cx="213" cy="300" rx="80" ry="40" fill="url(#logo-glow)"/>
        <path d="M46 352 Q200 318 380 334 L380 385 L46 385 Z" fill="url(#band-shadow)"/>
        <path d="M62 352 Q200 314 380 334" fill="none" stroke="var(--white)" stroke-width="4" stroke-linecap="round"/>
      </g>

      <g id="side-panel">
        <path fill="var(--blush)" d="M491 70 Q500 70 506 82 L605 240 L605 262 L380 262 L380 240 L476 82 Q482 70 491 70 Z"/>
        <circle cx="491" cy="82" r="3" fill="var(--white)"/>
        <rect x="495" y="118" width="4" height="42" fill="var(--white)"/>
        <g role="img" aria-label="Scattered white dot pattern">
          <ellipse cx="520" cy="210" rx="70" ry="45" fill="url(#dots-soft-light)"/>
        </g>
        <rect x="380" y="262" width="225" height="123" fill="var(--wine)"/>
        <path fill="var(--blush)" d="M380 385 L605 385 L605 402 L572 440 L572 545 L412 545 L412 440 L380 402 Z"/>
      </g>
    </defs>

    <path class="glue-tab" d="M46 262 L46 385 L4 372 L4 276 Z" fill="var(--white)" stroke="var(--tab-line)" stroke-width="1"/>

    <use href="#front-panel"/>
    <use href="#side-panel"/>
    <use href="#front-panel" x="559"/>
    <use href="#side-panel" x="560"/>

    <g role="img" aria-label="Small flourish ornament">
      <rect x="482" y="374" width="20" height="5" rx="2.5" fill="var(--blush)"/>
    </g>
  </svg>

  <div class="brand-mark front-a">Casa do Trufinho</div>
  <div class="brand-mark front-b">Casa do Trufinho</div>

  <section class="side-story">
    <h2>Text Text Text</h2>
    <p>Brazilian company interested in making the best Brigadeiros (Brazilian traditional sweet) in the country and also helping this little pieces of heaven become world famous one day! Brazilian company interested in making the best Brigadeiros (Brazilian traditional sweet) in the country and also helping this little pieces of heaven become world famous one day!</p>
  </section>
</main>
</body>
</html>
```